Flyer design

We need a marketing flyer to use when meeting with clients. We may also use it for mailings. Please see the attached document and images. Not all images need to be used. Please feel free to edit / photoshop images. Please also see our website : www.kelvorantissue.com

Industry/Entity Type

Marketing

```html
<!DOCTYPE html>
<html lang="en">
<head>
<meta charset="utf-8">
<title>Halvern Dermatology &amp; Dermatopathology – The Diagnosis in Focus</title>
<link rel="stylesheet" href="https://fonts.googleapis.com/css2?family=Arimo:wght@400;700&display=swap">
<style>
  :root {
    --paper: #ffffff;
    --ink: #1a1a1a;
    --accent: #e8232a;
    --band-a: #c2306e;
    --band-b: #e86aa0;
    --band-c: #f3a3c4;
    --frame: #1b1b1b;
    --portrait-dark: #2a2430;
    --portrait-mid: #6e6270;
    --tissue-pink: #d6707f;
    --tissue-light: #f0c0a8;
    --lens-yellow: #d9c98a;
    --lens-pale: #efe5b8;
  }
  * { box-sizing: border-box; margin: 0; padding: 0; }
  html, body { width: 932px; height: 1200px; overflow: hidden; background: var(--paper); }
  body { font-family: "Arimo", Arial, sans-serif; color: var(--ink); }
  .flyer { position: relative; width: 932px; height: 1200px; background: var(--paper); overflow: hidden; }

  .top-band {
    position: absolute; left: 0; top: 62px; width: 932px; height: 84px;
    background: linear-gradient(90deg, var(--band-b) 0%, var(--band-c) 30%, var(--band-a) 55%, #b0285f 80%, var(--band-b) 100%);
  }
  .headline { position: absolute; left: 0; top: 0; width: 932px; height: 146px; color: #fff; text-transform: uppercase; font-weight: 400; }
  .headline span { position: absolute; white-space: nowrap; }
  .headline .line-one { left: 468px; top: 81px; font-size: 27px; line-height: 27px; letter-spacing: 0.5px; }
  .headline .line-two { left: 598px; top: 103px; font-size: 47px; line-height: 47px; letter-spacing: 1px; }

  .brand { position: absolute; left: 100px; top: 188px; width: 396px; text-align: center; text-transform: uppercase; }
  .brand-name { display: block; color: var(--accent); font-size: 19px; line-height: 22px; letter-spacing: 22px; margin-right: -22px; }
  .brand-sub { display: block; color: var(--ink); font-size: 17px; line-height: 22px; margin-top: 2px; }

  .profile {
    position: absolute; left: 70px; top: 262px; width: 782px; height: 244px;
    border: 5px solid var(--frame);
    background: linear-gradient(100deg, var(--portrait-dark) 0%, #4a3f4e 40%, var(--portrait-mid) 60%, #3c3440 100%);
  }
  .portrait {
    position: absolute; right: 0; top: 0; width: 300px; height: 100%;
    background: radial-gradient(ellipse at 55% 40%, #c9a98e 0%, #7b6a6a 40%, #2b2733 80%);
  }
  .profile-text { position: absolute; left: 13px; top: 52px; color: #fff; text-transform: uppercase; }
  .profile-name { font-size: 24px; line-height: 26px; }
  .profile-cred { font-size: 20px; line-height: 25px; }
  .profile-since { font-size: 20px; line-height: 24px; margin-top: 9px; margin-left: 3px; }

  .intro {
    position: absolute; left: 150px; top: 546px; width: 640px;
    font-size: 21px; line-height: 26px; text-transform: uppercase;
  }
  .intro span { display: block; text-align: justify; text-align-last: justify; white-space: nowrap; }
  .intro span.last { text-align: center; text-align-last: center; }

  .services {
    position: absolute; left: 170px; top: 675px; width: 600px; list-style: none;
    text-align: center; text-transform: uppercase; font-size: 20px; line-height: 25px;
  }
  .services li { margin-bottom: 9px; }

  .lens {
    position: absolute; width: 170px; height: 170px; border-radius: 50%;
    border: 4px solid var(--frame);
  }
  .lens-left { left: 36px; top: 721px; background: radial-gradient(circle at 45% 45%, var(--tissue-light) 0%, var(--tissue-pink) 55%, #a94a5c 100%); }
  .lens-right { left: 711px; top: 721px; background: radial-gradient(circle at 50% 50%, var(--lens-pale) 0%, var(--lens-yellow) 60%, #8d7d4a 100%); }

  .closing {
    position: absolute; left: 16px; top: 947px; width: 900px; text-align: center;
    font-size: 19px; line-height: 25px; text-transform: uppercase;
  }
  .closing em { font-style: normal; color: var(--accent); }

  .bottom-band {
    position: absolute; left: 0; top: 1031px; width: 932px; height: 101px;
    background: linear-gradient(90deg, var(--band-b) 0%, var(--band-a) 35%, #d4548a 65%, var(--band-c) 100%);
    color: #fff; text-align: center; text-transform: uppercase; font-size: 14px; letter-spacing: 0.8px;
    padding-top: 28px; line-height: 27px;
  }
</style>
</head>
<body>
<main class="flyer">
  <div class="top-band"></div>
  <h1 class="headline"><span class="line-one">The Diagnosis</span><span class="line-two">In Focus</span></h1>

  <p class="brand">
    <span class="brand-name">Halvern</span>
    <span class="brand-sub">Dermatology &amp; Dermatopathology</span>
  </p>

  <section class="profile">
    <div class="portrait" role="img" aria-label="Portrait photograph of the dermatopathologist in a suit"></div>
    <div class="profile-text">
      <p class="profile-name">Ren T. Malloway, M.D.</p>
      <p class="profile-cred">Board Certified – Dermatopathology</p>
      <p class="profile-cred">Board Certified – Dermatology</p>
      <p class="profile-since">Practicing Dermatopathology<br>since 2007.</p>
    </div>
  </section>

  <p class="intro">
    <span>Commitment to helping find solutions, either</span>
    <span>in&#8209;house or through our contacts, for all</span>
    <span>your dermatopathology needs including but</span>
    <span class="last">not limited to:</span>
  </p>

  <div class="lens lens-left" role="img" aria-label="Microscope view of stained skin tissue"></div>
  <div class="lens lens-right" role="img" aria-label="Microscope view of a tissue section on a slide"></div>

  <ul class="services">
    <li>Dermatopathology consultative service,<br>first or second opinions,<br>off-site or on-site</li>
    <li>Tissue processing</li>
    <li>Mohs technicians</li>
    <li>Immunohistochemistry<br>and special stains</li>
  </ul>

  <p class="closing"><em>Access</em> to an extensive range of special and immunohistochemistry<br>stains, and <em>patient-centered</em> consideration of the judicious use of them.</p>

  <footer class="bottom-band">
    <p>Usually 2-3 day turnaround time depending on the circumstance of the case.</p>
    <p>Courier pick up can usually be arranged.</p>
  </footer>
</main>
</body>
</html>
```